Postcard Design to introduce Plinkett Drip Solutions services

Company name: Indoor Water ConservationCustom fitted products for sinks, showers and toilets.Average savings 20%ROI 6 to 12 monthsNote: we just joined this organization and want to use this postcard to "introduce" our Company and services so that when they think of conserving water indoors, they think of use. In your images section are our logo (we have other resolutions if needed) and an image - we are open to suggestions for design and what to include.One suggestion is to introduce us and use the New Years Resolution - even if conserving water and saving money are not our new year's resolution, when you are ready to conserve water and save money, think of us.

Target Market(s)

2 markets - 1) hotels and 2) apartment complexes. 2 markets, 2 postcards, 2 mailing lists

Industry/Entity Type

It Company

Colors
85acd3
33a6d7
33b8a4

Requirements
Must have
• logo, company name, ave savings 20%, ROI 6 - 12 months, introduction that we are new service provider to 1) Marrowby Innkeepers and Hospitality Association (1 mailing/1 postcard) and new service provider to 2) Tellaview Rental Housing Association (2nd mailing/2nd postcard).
Nice to have
• Using the concept of New Year's resolution, maybe a finger with a string tied to it about to turn off a faucet - or some similar image.

```html
<!DOCTYPE html>
<html lang="en">
<head>
<meta charset="utf-8">
<title>Plinkett Drip Solutions – Postcard</title>
<link rel="stylesheet" href="https://fonts.googleapis.com/css2?family=Lato:ital,wght@0,400;0,700;0,900;1,700;1,900&display=swap">
<style>
  :root {
    --brand-blue: #1f7cc6;
    --brand-deep: #1565b0;
    --brand-sky: #33a6d7;
    --brand-soft: #85acd3;
    --brand-teal: #33b8a4;
    --ink: #222a33;
    --paper: #ffffff;
    --backdrop: #ecebe8;
    --line: #9a9a9a;
  }
  * { box-sizing: border-box; margin: 0; padding: 0; }
  html, body { width: 907px; height: 1200px; overflow: hidden; }
  body {
    background: var(--backdrop);
    font-family: "Lato", Arial, sans-serif;
    position: relative;
  }
  .postcard {
    position: absolute;
    left: 123px;
    width: 662px;
    height: 513px;
    background: var(--paper);
    overflow: hidden;
    box-shadow: 0 3px 10px rgba(0,0,0,.18);
  }
  .postcard--front { top: 57px; }
  .postcard--back { top: 622px; }
  .postcard > * { position: absolute; }
  .waves { left: 0; top: 0; width: 662px; height: 513px; }

  /* front */
  .brand { left: 52px; top: 62px; display: flex; align-items: center; gap: 10px; }
  .brand__dot { width: 46px; height: 46px; border-radius: 50%; background: var(--brand-sky); }
  .brand__name { font-weight: 900; font-size: 24px; line-height: 1.05; color: var(--brand-blue); width: 170px; }
  .offer { left: 345px; top: 24px; color: #fff; white-space: nowrap; }
  .offer__line { display: flex; align-items: center; gap: 8px; }
  .offer__pct { font-weight: 900; font-size: 50px; line-height: 1; letter-spacing: -1px; }
  .offer__label { font-size: 20px; font-weight: 400; text-transform: uppercase; letter-spacing: .3px; }
  .offer__roi { font-size: 32px; font-weight: 700; margin-top: 2px; }
  .hero-photo {
    left: 330px; top: 130px; width: 332px; height: 330px;
    background: radial-gradient(ellipse at 45% 50%, #e8f3fb 0%, #a9d3ee 45%, #4d9bd0 100%);
  }
  .tag {
    background: var(--brand-blue); color: #fff; font-size: 19px; text-transform: uppercase;
    padding: 2px 26px 2px 24px; border-radius: 0 14px 14px 0; letter-spacing: .2px;
    white-space: nowrap; line-height: 1.25;
  }
  .tag--provide { left: 0; top: 276px; }
  .provide__title { left: 24px; top: 312px; font-style: italic; font-weight: 700; font-size: 23px; color: var(--ink); white-space: nowrap; }
  .provide__list { left: 24px; top: 349px; list-style: none; display: flex; gap: 18px; color: var(--brand-deep); font-size: 19px; }
  .provide__list li::before { content: "●"; font-size: 13px; color: var(--brand-sky); margin-right: 12px; vertical-align: 2px; }
  .call { left: 24px; top: 456px; display: flex; align-items: center; color: #fff; white-space: nowrap; }
  .call__text { font-style: italic; font-weight: 700; font-size: 19px; }
  .call__icon { margin: 0 16px 0 18px; }
  .call__number { font-size: 35px; font-weight: 700; letter-spacing: .5px; }

  /* back */
  .tag--company { left: 0; top: 27px; width: 292px; font-size: 16px; padding-left: 22px; }
  .intro { left: 21px; top: 61px; font-style: italic; font-weight: 700; font-size: 14px; color: var(--ink); }
  .members { left: 49px; top: 90px; list-style: none; font-size: 12.5px; color: var(--ink); line-height: 23px; }
  .reminder-art { left: 0; top: 152px; width: 100px; height: 100px;
    background: linear-gradient(135deg, #f6f6f6, #e2e2e2); }
  .resolution { left: 104px; top: 172px; font-style: italic; font-weight: 900; font-size: 30px; line-height: 1.25; color: var(--brand-sky); }
  .pitch { left: 17px; top: 274px; width: 252px; font-style: italic; font-weight: 700; font-size: 12px; line-height: 1.35; color: var(--ink); }
  .pitch strong { display: block; font-style: normal; color: var(--brand-blue); font-weight: 700; }
  .contact { left: 0; top: 362px; width: 278px; height: 72px; background: var(--brand-sky);
    list-style: none; padding: 3px 0 0 22px; color: #fff; font-size: 12.5px; font-weight: 700; line-height: 21px; }
  .contact li { display: flex; align-items: center; gap: 10px; }
  .contact svg { flex: none; }
  .dove-art { left: 225px; top: 290px; width: 130px; height: 170px; border-radius: 50%;
    background: radial-gradient(ellipse at 50% 50%, rgba(159,208,239,.8) 0%, rgba(200,230,248,.5) 45%, rgba(255,255,255,0) 70%); }
  .stamp { left: 543px; top: 60px; width: 86px; height: 90px; border: 1px solid var(--line); }
  .address-line { left: 387px; width: 243px; height: 0; border-top: 1px solid var(--line); }
  .address-line--1 { top: 238px; }
  .address-line--2 { top: 278px; }
  .address-line--3 { top: 320px; }
</style>
</head>
<body>

<section class="postcard postcard--front" aria-label="Postcard front">
  <svg class="waves" viewBox="0 0 662 513" aria-hidden="true">
    <path d="M0,128 C80,190 230,200 335,138 C240,212 90,205 0,172 Z" fill="var(--brand-teal)"/>
    <path d="M0,172 C100,250 250,232 340,150 C265,248 120,272 0,255 Z" fill="var(--brand-blue)"/>
  </svg>
  <div class="hero-photo" role="img" aria-label="Cupped hands holding a glass bowl of splashing water with the Earth inside"></div>
  <svg class="waves" viewBox="0 0 662 513" aria-hidden="true">
    <path d="M262,0 C285,75 325,128 420,146 C520,166 600,132 662,148 L662,0 Z" fill="var(--brand-blue)"/>
    <path d="M328,138 C365,155 395,160 420,146 C520,166 600,132 662,148 L662,162 C600,146 520,182 415,160 C380,158 350,150 328,138 Z" fill="var(--brand-teal)"/>
    <path d="M0,372 C160,420 420,438 662,428 L662,438 C420,450 160,432 0,386 Z" fill="var(--brand-sky)"/>
    <path d="M0,392 C180,438 420,438 662,445 L662,513 L0,513 Z" fill="#fff"/>
    <path d="M0,402 C190,442 420,420 662,455 L662,513 L0,513 Z" fill="var(--brand-sky)"/>
    <path d="M0,416 C200,446 420,425 662,464 L662,513 L0,513 Z" fill="var(--brand-blue)"/>
  </svg>

  <div class="brand">
    <span class="brand__dot"></span>
    <span class="brand__name">Plinkett Drip Solutions</span>
  </div>

  <div class="offer">
    <div class="offer__line"><span class="offer__pct">20%</span><span class="offer__label">Average Savings</span></div>
    <div class="offer__roi">ROI 6 to 12 months</div>
  </div>

  <div class="tag tag--provide">We Provide</div>
  <p class="provide__title">Custom fitted products for</p>
  <ul class="provide__list">
    <li>Sinks</li><li>Showers</li><li>Toilets</li>
  </ul>

  <div class="call">
    <span class="call__text">Call Us Now for more information</span>
    <svg class="call__icon" width="22" height="22" viewBox="0 0 24 24" aria-hidden="true">
      <path d="M6.6 10.8c1.4 2.8 3.8 5.1 6.6 6.6l2.2-2.2c.3-.3.7-.4 1-.2 1.1.4 2.3.6 3.6.6.6 0 1 .4 1 1V20c0 .6-.4 1-1 1C10.6 21 3 13.4 3 4c0-.6.4-1 1-1h3.5c.6 0 1 .4 1 1 0 1.3.2 2.5.6 3.6.1.3 0 .7-.2 1z" fill="var(--brand-teal)"/>
    </svg>
    <span class="call__number">0198765432</span>
  </div>
</section>

<section class="postcard postcard--back" aria-label="Postcard back">
  <svg class="waves" viewBox="0 0 662 513" aria-hidden="true">
    <path d="M352,0 C380,120 330,230 262,330 C310,250 360,140 330,0 Z" fill="var(--brand-teal)"/>
    <path d="M375,0 C400,130 350,250 270,350 C330,260 370,140 352,0 Z" fill="var(--brand-blue)"/>
    <path d="M395,0 C410,120 370,230 290,340 C345,250 385,140 375,0 Z" fill="var(--brand-sky)"/>
  </svg>

  <div class="tag tag--company">Plinkett Drip Solutions</div>
  <p class="intro">We are new service provider to</p>
  <ul class="members">
    <li>Marrowby Innkeepers and Hospitality Association</li>
    <li>Tellaview Rental Housing Association</li>
  </ul>

  <div class="reminder-art" role="img" aria-label="Line drawing of a finger with a string tied around it"></div>
  <h2 class="resolution">New Years<br>Resolution</h2>

  <p class="pitch">Even if conserving water and saving money are not our new year's resolution, when you are ready to conserve water and save money, <strong>THINK OF US</strong></p>

  <ul class="contact">
    <li><svg width="10" height="10" viewBox="0 0 24 24" aria-hidden="true"><path d="M6.6 10.8c1.4 2.8 3.8 5.1 6.6 6.6l2.2-2.2c.3-.3.7-.4 1-.2 1.1.4 2.3.6 3.6.6.6 0 1 .4 1 1V20c0 .6-.4 1-1 1C10.6 21 3 13.4 3 4c0-.6.4-1 1-1h3.5c.6 0 1 .4 1 1 0 1.3.2 2.5.6 3.6.1.3 0 .7-.2 1z" fill="var(--brand-teal)"/></svg>0198765432</li>
    <li><svg width="10" height="8" viewBox="0 0 20 14" aria-hidden="true"><rect width="20" height="14" fill="var(--brand-teal)"/><path d="M0,0 L10,8 L20,0" fill="none" stroke="#fff" stroke-width="2"/></svg>info@plinkettdrip.example</li>
    <li><svg width="10" height="10" viewBox="0 0 20 20" aria-hidden="true"><circle cx="10" cy="10" r="9" fill="var(--brand-teal)"/></svg>www.plinkettdrip.example</li>
  </ul>

  <div class="dove-art" role="img" aria-label="Dove shaped from splashing water"></div>

  <div class="stamp" aria-hidden="true"></div>
  <div class="address-line address-line--1"></div>
  <div class="address-line address-line--2"></div>
  <div class="address-line address-line--3"></div>
</section>

</body>
</html>
```